Business Card Design with new logo

Dorian Pelleway 4172
E 118th St Ashbrook, IL 62418
Cell: 217-555-0193
pellewayrestoration@mailvane.test

Classic Car Restoration Services Buy Sell Trade Consign

Dorian Pelleway 9698
Cell: 217-555-0193

```html
<!DOCTYPE html>
<html lang="en">
<head>
<meta charset="utf-8">
<title>Pelleway Restoration LLC — Business Cards</title>
<link href="https://fonts.googleapis.com/css2?family=Open+Sans:ital,wght@0,400;0,600;0,700;0,800;1,700&display=swap" rel="stylesheet">
<style>
  :root {
    --backdrop: #3b3b3d;
    --card-white: #ffffff;
    --brand-red: #c0373a;
    --ink-dark: #2c3440;
    --text-light: #ffffff;
    --band-text-dark: #2a2a2e;
  }
  * { box-sizing: border-box; margin: 0; padding: 0; }
  html, body {
    width: 1200px; height: 801px; overflow: hidden;
    background: var(--backdrop);
    font-family: "Open Sans", Arial, sans-serif;
  }
  .canvas { position: relative; width: 1200px; height: 801px; }
  .card {
    position: absolute; top: 260px; width: 494px; height: 281px;
    border-radius: 12px; overflow: hidden;
  }
  .card--front { left: 89px; background: var(--card-white); }
  .card--back { left: 620px; background: var(--brand-red); }

  .brand {
    position: absolute; left: 0; right: 0; text-align: center;
    color: var(--ink-dark); font-weight: 800;
  }
  .card--front .brand { top: 60px; }
  .card--back .brand { top: 40px; }
  .brand__mark {
    display: block; width: 54px; height: 54px; margin: 0 auto 12px;
    border-radius: 50%; background: var(--brand-red);
  }
  .card--back .brand__mark { background: var(--card-white); }
  .brand__name { display: block; font-size: 36px; line-height: 1; letter-spacing: 1px; text-transform: uppercase; }
  .brand__sub { display: block; font-size: 12.5px; letter-spacing: 6px; text-transform: uppercase; margin-top: 8px; }
  .card--back .brand__name { font-size: 30px; }
  .card--back .brand__sub { font-size: 11px; letter-spacing: 5px; margin-top: 6px; }

  .contact {
    position: absolute; left: 0; right: 0; top: 181px;
    color: var(--text-light); font-size: 12px; font-weight: 700;
    text-align: center; line-height: 21px;
  }
  .contact__row { display: flex; justify-content: center; gap: 8px; }
  .contact__item { display: inline-flex; align-items: center; gap: 4px; }
  .contact__icon { width: 11px; height: 11px; flex: none; }

  .tagline-band {
    position: absolute; left: 0; right: 0; top: 235px; height: 26px;
    display: flex; align-items: center; justify-content: center;
    font-size: 13.5px; font-weight: 700; font-style: italic;
  }
  .card--front .tagline-band { background: var(--brand-red); color: var(--text-light); }
  .card--back .tagline-band { background: var(--card-white); color: var(--band-text-dark); }
</style>
</head>
<body>
<main class="canvas">
  <section class="card card--front">
    <div class="brand">
      <span class="brand__mark"></span>
      <span class="brand__name">Pelleway</span>
      <span class="brand__sub">Restoration LLC</span>
    </div>
    <div class="tagline-band">Classic Car Restoration Services Buy Sell Trade Consign</div>
  </section>

  <section class="card card--back">
    <div class="brand">
      <span class="brand__mark"></span>
      <span class="brand__name">Pelleway</span>
      <span class="brand__sub">Restoration LLC</span>
    </div>
    <div class="contact">
      <div class="contact__row">
        <span class="contact__item">
          <svg class="contact__icon" viewBox="0 0 12 12"><circle cx="6" cy="6" r="6" fill="#2a2a2e"/><path d="M6 2.5a2 2 0 0 0-2 2c0 1.5 2 4 2 4s2-2.5 2-4a2 2 0 0 0-2-2z" fill="#c0373a"/></svg>
          Dorian Pelleway 4172
        </span>
        <span class="contact__item">
          <svg class="contact__icon" viewBox="0 0 12 12"><circle cx="6" cy="6" r="6" fill="#2a2a2e"/><path d="M3 6h6M6 3l3 3-3 3" stroke="#c0373a" stroke-width="1.4" fill="none"/></svg>
          E 118th St Ashbrook, IL 62418
        </span>
      </div>
      <div class="contact__row">
        <span class="contact__item">
          <svg class="contact__icon" viewBox="0 0 12 12"><circle cx="6" cy="6" r="6" fill="#2a2a2e"/><path d="M4 3.2l1.2 1.4-.6.8a4 4 0 0 0 2 2l.8-.6L8.8 8 8 9a5 5 0 0 1-5-5z" fill="#c0373a"/></svg>
          217-555-0193
        </span>
        <span class="contact__item">
          <svg class="contact__icon" viewBox="0 0 12 12"><circle cx="6" cy="6" r="6" fill="#2a2a2e"/><rect x="3" y="4" width="6" height="4.2" fill="none" stroke="#c0373a" stroke-width="1"/><path d="M3 4l3 2.3L9 4" stroke="#c0373a" stroke-width="1" fill="none"/></svg>
          pellewayrestoration@mailvane.test
        </span>
      </div>
    </div>
    <div class="tagline-band">Classic Car Restoration Services Buy Sell Trade Consign</div>
  </section>
</main>
</body>
</html>
```